Business cards to launch an education platform

Hi,
I am looking at having new business cards designed.
I am a startup, developing a web platform for schools and university, the education world. It's an online assessment system.
I would like a card that looks classy, and that is using the colors and the font of my logo.

I have attached:
1) my logo
2) A business card that I have designed quickly so you can have all the information required in the card, but I really don't like it.
3) The font that I am using (Lato Regular) to design my web platform
4) Some screenshots of my web platform so you can have a look at the style that I have.

Target Market(s)

Major market: Education system: Schools and university
Minor markets: Business in general

Industry/Entity Type

Business

Contact Information for Business Card

Lydia Marsh
Director

M: 0437 681 902
E: lydia.marsh@copperLeafSystems.com.au

Requirements
Must have
• The colors of my logo

```html
<!DOCTYPE html>
<html lang="en">
<head>
<meta charset="utf-8">
<title>Copper Leaf Systems – Business Cards</title>
<link rel="stylesheet" href="https://fonts.googleapis.com/css2?family=Lato:wght@400;700&display=swap">
<style>
  :root {
    --page-bg: #ecebe8;
    --card-white: #ffffff;
    --brand-blue: #0654a3;
    --brand-navy: #0b3f73;
    --brand-cyan: #23c4ef;
    --brand-dark-line: #0a2f57;
    --text-dark: #333333;
    --text-body: #3a3a3a;
    --icon-blue: #1c63b0;
  }
  * { box-sizing: border-box; margin: 0; padding: 0; }
  html, body {
    width: 964px;
    height: 1200px;
    overflow: hidden;
    background: var(--page-bg);
    font-family: "Lato", Arial, sans-serif;
  }
  .canvas { position: relative; width: 964px; height: 1200px; }

  .card {
    position: absolute;
    width: 740px;
    height: 456px;
    background: var(--card-white);
    overflow: hidden;
    box-shadow: 0 1px 4px rgba(0,0,0,0.12);
  }

  /* ---------- Front card ---------- */
  .card-front { left: 108px; top: 90px; }
  .front-panel {
    position: absolute; left: 0; top: 0;
    width: 225px; height: 100%;
    background: var(--brand-blue);
  }
  .front-stripe-cyan {
    position: absolute; left: 225px; top: 0;
    width: 5px; height: 100%;
    background: var(--brand-cyan);
  }
  .front-stripe-dark {
    position: absolute; left: 230px; top: 0;
    width: 5px; height: 100%;
    background: var(--brand-dark-line);
  }
  .front-brand-square {
    position: absolute; left: 150px; top: 118px;
    width: 150px; height: 150px;
    background: var(--brand-blue);
    border: 8px solid var(--card-white);
  }
  .front-brand-name {
    position: absolute; left: 337px; top: 142px;
    color: var(--brand-navy);
    font-weight: 400;
    font-size: 48px;
    line-height: 56px;
    letter-spacing: 3px;
  }
  .front-url {
    position: absolute; left: 255px; top: 372px;
    color: var(--brand-navy);
    font-weight: 700;
    font-size: 23px;
  }

  /* ---------- Back card ---------- */
  .card-back { left: 110px; top: 635px; height: 455px; }
  .back-band-top {
    position: absolute; left: 0; top: 0;
    width: 100%; height: 56px;
    background: var(--brand-blue);
  }
  .back-line-cyan {
    position: absolute; left: 0; top: 57px;
    width: 100%; height: 4px;
    background: var(--brand-cyan);
  }
  .back-line-dark {
    position: absolute; left: 0; top: 62px;
    width: 100%; height: 4px;
    background: var(--brand-dark-line);
  }
  .back-band-bottom {
    position: absolute; left: 0; bottom: 0;
    width: 100%; height: 38px;
    background: var(--brand-blue);
  }
  .back-brand-square {
    position: absolute; left: 70px; top: 42px;
    width: 96px; height: 96px;
    background: var(--brand-blue);
    border: 6px solid var(--card-white);
  }
  .back-brand-name {
    position: absolute; left: 177px; top: 70px;
    color: var(--brand-navy);
    font-weight: 400;
    font-size: 29px;
    line-height: 33px;
    letter-spacing: 2px;
  }
  .contact-person { position: absolute; left: 84px; top: 200px; }
  .contact-name {
    color: var(--text-dark);
    font-weight: 700;
    font-size: 21px;
    line-height: 26px;
  }
  .contact-role {
    color: var(--text-body);
    font-size: 21px;
    line-height: 28px;
  }
  .contact-list {
    position: absolute; left: 82px; top: 270px;
    list-style: none;
  }
  .contact-item {
    display: flex; align-items: center; gap: 8px;
    color: var(--text-body);
    font-size: 20.5px;
    height: 31.5px;
  }
  .contact-icon { width: 20px; height: 20px; flex: none; }
</style>
</head>
<body>
<main class="canvas">

  <section class="card card-front" aria-label="Business card front">
    <div class="front-panel"></div>
    <div class="front-stripe-cyan"></div>
    <div class="front-stripe-dark"></div>
    <div class="front-brand-square" aria-hidden="true"></div>
    <div class="front-brand-name">COPPER LEAF<br>Systems</div>
    <div class="front-url">www.copperLeafSystems.com.au</div>
  </section>

  <section class="card card-back" aria-label="Business card back">
    <div class="back-band-top"></div>
    <div class="back-line-cyan"></div>
    <div class="back-line-dark"></div>
    <div class="back-brand-square" aria-hidden="true"></div>
    <div class="back-brand-name">COPPER LEAF<br>Systems</div>

    <div class="contact-person">
      <p class="contact-name">Lydia Marsh</p>
      <p class="contact-role">Director</p>
    </div>

    <ul class="contact-list">
      <li class="contact-item">
        <svg class="contact-icon" viewBox="0 0 20 20" aria-hidden="true">
          <rect x="5" y="2" width="11" height="16" rx="2" fill="none" stroke="var(--icon-blue)" stroke-width="1.6"/>
          <line x1="8.5" y1="15" x2="12.5" y2="15" stroke="var(--icon-blue)" stroke-width="1.4"/>
        </svg>
        <span>0437 681 902</span>
      </li>
      <li class="contact-item">
        <svg class="contact-icon" viewBox="0 0 20 20" aria-hidden="true">
          <rect x="2" y="5" width="16" height="11" fill="none" stroke="var(--icon-blue)" stroke-width="1.6"/>
          <polyline points="2,5 10,12 18,5" fill="none" stroke="var(--icon-blue)" stroke-width="1.6"/>
        </svg>
        <span>lydia.marsh@copperLeafSystems.com.au</span>
      </li>
      <li class="contact-item">
        <svg class="contact-icon" viewBox="0 0 20 20" aria-hidden="true">
          <circle cx="10" cy="10" r="8" fill="none" stroke="var(--icon-blue)" stroke-width="1.6"/>
          <ellipse cx="10" cy="10" rx="3.5" ry="8" fill="none" stroke="var(--icon-blue)" stroke-width="1.3"/>
          <line x1="2" y1="10" x2="18" y2="10" stroke="var(--icon-blue)" stroke-width="1.3"/>
        </svg>
        <span>www.copperLeafSystems.com.au</span>
      </li>
    </ul>

    <div class="back-band-bottom"></div>
  </section>

</main>
</body>
</html>
```